I would like a stylish low key card that represents my Cedar Nook. A boutique rental property . This property is of the highest standard and I wish the card to covey this without being old fashion

Boutique

Tessa Varrow
0427350192
tessa.varrow@varrow.com.au Cedar Nook

```html
<!DOCTYPE html>
<html lang="en">
<head>
<meta charset="utf-8">
<title>Tessa Varrow – The Cedar Nook</title>
<link rel="stylesheet" href="https://fonts.googleapis.com/css2?family=Abril+Fatface&family=Noto+Serif:wght@400&display=swap">
<style>
  :root {
    --paper: #ffffff;
    --ink: #1a1a1a;
    --band: #1c1c1c;
    --sage: #b9bc95;
  }
  html, body {
    margin: 0;
    padding: 0;
    overflow: hidden;
    background: var(--paper);
  }
  .card {
    position: relative;
    width: 1200px;
    height: 693px;
    background: var(--paper);
    overflow: hidden;
  }
  .owner-name {
    position: absolute;
    right: 51px;
    top: 62px;
    margin: 0;
    font-family: "Abril Fatface", "Bodoni Moda", serif;
    font-weight: 400;
    font-size: 62px;
    line-height: 1;
    color: var(--ink);
    letter-spacing: -0.5px;
  }
  .rule {
    position: absolute;
    left: 0;
    width: 1200px;
    background: var(--ink);
  }
  .rule--top { top: 160px; height: 19px; }
  .rule--bottom { top: 438px; height: 18px; }
  .brand-band {
    position: absolute;
    left: 0;
    top: 193px;
    width: 1200px;
    height: 229px;
    background: var(--band);
    display: flex;
    align-items: center;
    padding-left: 104px;
    box-sizing: border-box;
  }
  .brand-name {
    margin: 0;
    font-family: "Noto Serif", Georgia, serif;
    font-weight: 400;
    font-size: 104px;
    line-height: 1;
    color: var(--sage);
    letter-spacing: 2px;
  }
  .contact {
    position: absolute;
    left: 47px;
    top: 462px;
    margin: 0;
    font-family: "Noto Serif", Georgia, serif;
    font-size: 45px;
    line-height: 63px;
    color: var(--ink);
    font-style: normal;
  }
  .contact span { display: block; }
</style>
</head>
<body>
  <main class="card">
    <h1 class="owner-name">Tessa Varrow</h1>
    <div class="rule rule--top"></div>
    <div class="brand-band">
      <p class="brand-name">The Cedar Nook</p>
    </div>
    <div class="rule rule--bottom"></div>
    <address class="contact">
      <span class="contact-phone">tel: 0427350192</span>
      <span class="contact-email">tessa.varrow@varrow.com.au</span>
    </address>
  </main>
</body>
</html>
```